Tall Cedar Builders Business Card

I'm looking for a business card design for a start-up Handyman/Construction Company. The organization will double as a ministry to the homeless, hoping to create job opportunity and training to the homeless, providing a pathway back to being "homed". I'm looking for a simple to "seeming" simple design. Open to all thoughts.

Industry/Entity Type

Ministry

Requirements
Must have
• Logo (Attached), Name, Phone, Email and Address. Note - "*Registered and Insured".

```html
<!DOCTYPE html>
<html lang="en">
<head>
<meta charset="utf-8">
<title>Tall Cedar Builders Business Card</title>
<link href="https://fonts.googleapis.com/css2?family=Fira+Sans:wght@400;700&display=swap" rel="stylesheet">
<style>
  :root {
    --page-bg: #2a2a2a;
    --card-white: #ffffff;
    --navy: #1f3256;
    --purple: #6a2b86;
    --text-light: #ffffff;
    --brand-ink: #1f3256;
  }
  html, body {
    margin: 0;
    padding: 0;
    width: 1200px;
    height: 902px;
    overflow: hidden;
    background: var(--page-bg);
  }
  .stage {
    width: 1200px;
    height: 902px;
    display: flex;
    align-items: center;
    justify-content: center;
  }
  .business-card {
    width: 1000px;
    height: 567px;
    display: block;
    box-shadow: 0 6px 24px rgba(0,0,0,0.5);
    font-family: "Fira Sans", sans-serif;
  }
  .brand-name { font-weight: 700; font-size: 21px; fill: var(--brand-ink); letter-spacing: 0.2px; }
  .brand-sub { font-weight: 400; font-size: 3.6px; fill: var(--brand-ink); }
  .holder-name { font-weight: 400; font-size: 14px; fill: var(--text-light); }
  .holder-title { font-weight: 400; font-size: 6px; fill: var(--text-light); }
  .contact { font-weight: 400; font-size: 7.6px; fill: var(--text-light); }
</style>
</head>
<body>
<main class="stage">
  <svg class="business-card" viewBox="0 0 344 195" xmlns="http://www.w3.org/2000/svg" role="group" aria-label="Tall Cedar Builders business card">
    <defs>
      <linearGradient id="panel-gradient" x1="0" y1="1" x2="1" y2="0">
        <stop offset="0" stop-color="var(--purple)"/>
        <stop offset="0.65" stop-color="#3b2d6a"/>
        <stop offset="1" stop-color="var(--navy)"/>
      </linearGradient>
    </defs>

    <rect class="card-base" x="0" y="0" width="344" height="195" fill="var(--card-white)"/>
    <polygon class="accent-band" points="210,0 344,0 344,195 52,195" fill="var(--navy)"/>
    <polygon class="info-panel" points="238,0 344,0 344,195 90,195" fill="url(#panel-gradient)"/>

    <g class="brand">
      <text class="brand-name" x="20" y="40">Tall Cedar</text>
      <text class="brand-sub" x="131" y="47" text-anchor="end">Builders, LLC</text>
    </g>

    <g class="holder">
      <text class="holder-name" x="297" y="48" text-anchor="end">Your Name</text>
      <line x1="220" y1="51" x2="297" y2="51" stroke="var(--text-light)" stroke-width="0.6"/>
      <text class="holder-title" x="286" y="59" text-anchor="end">Founder &amp; CEO</text>
    </g>

    <g class="contact-block">
      <text class="contact" x="301" y="90" text-anchor="end">Telephone:</text>
      <text class="contact" x="301" y="99" text-anchor="end">0123.456.789</text>
      <text class="contact" x="301" y="117" text-anchor="end">Address:</text>
      <text class="contact" x="301" y="126" text-anchor="end">19xx street line,</text>
      <text class="contact" x="301" y="135" text-anchor="end">City Name - Zipcode,</text>
      <text class="contact" x="301" y="144" text-anchor="end">Country</text>
      <text class="contact" x="301" y="166" text-anchor="end">Email: name@mail.com</text>
      <text class="contact" x="301" y="185" text-anchor="end">www.sitename.com</text>
    </g>
  </svg>
</main>
</body>
</html>
```